COVID-19 Accredited CME Impact Infographic

We want an infographic showing how much COVID-19 Continuing Medical Education we have accredited and its impact. Our website is at https://health.quillmere.edu/cme/COVID19/education.html The attached document is intended to simply show the elements. You have complete freedom on design. We will be updating the numbers weekly so it is important that we have the files so that we can update it. This can be done in powerpoint, publisher, word, in-design, illustrator. Don't use crazy fonts that we wont have.

Target Market(s)

Internal to Quillmere. We just want to show the impact of our work

Industry/Entity Type

Education

Requirements
Must have
• We must be able to update the numbers ourselves.

See attached document for the pieces that we want.

The sizes of the numbers in the attached are based on importance to us.
Nice to have
• Not mandatory but try to use these colors. https://health.quillmere.edu/identity/color-palette.html

I was thinking that perhaps the big number could be done in traditional train. Like this: https://www.pixelvault.com/image-illustration/flip-board-under-constuction-page-isolated-8830417265

```html
<!DOCTYPE html>
<html lang="en">
<head>
<meta charset="utf-8">
<title>COVID-19 CME Impact</title>
<link href="https://fonts.googleapis.com/css2?family=Source+Sans+3:wght@300;400;500;600;700&display=swap" rel="stylesheet">
<style>
  :root {
    --teal-dark: #3f8f8c;
    --teal-light: #a9dcc6;
    --olive: #7d9a3a;
    --sky: #2a9bc4;
    --navy: #163a55;
    --cardinal: #8c1515;
    --virus: #b8232a;
    --white: #ffffff;
    --edge: #d9d9d9;
  }
  * { box-sizing: border-box; margin: 0; padding: 0; }
  html, body { width: 1200px; height: 923px; overflow: hidden; background: var(--white); }
  body { font-family: "Source Sans 3", "Source Sans Pro", Arial, sans-serif; }
  .infographic {
    position: relative; width: 1200px; height: 923px;
    border: 2px solid var(--edge); overflow: hidden; background: var(--white);
  }
  .header {
    position: absolute; left: 0; top: 0; width: 100%; height: 164px;
    background: linear-gradient(90deg, var(--teal-dark) 0%, var(--teal-light) 45%, #8fcfb7 70%, #5d9f95 100%);
  }
  .header-virus {
    position: absolute; right: 0; top: 0; width: 188px; height: 164px;
    background: radial-gradient(circle at 70% 45%, var(--virus) 0%, #7a1a1e 40%, rgba(90,140,130,0) 72%);
  }
  .brand {
    position: absolute; left: 52px; top: 92px; display: flex; align-items: center; gap: 8px;
    color: var(--cardinal); font-weight: 600; font-size: 24px; line-height: 1;
  }
  .brand-mark { width: 16px; height: 16px; background: var(--cardinal); }
  .title {
    position: absolute; left: 318px; top: 38px;
    font-weight: 300; font-size: 92px; line-height: 1; color: var(--white); white-space: nowrap;
  }
  .reach-number {
    position: absolute; top: 249px; font-size: 112px; font-weight: 400; line-height: 1; color: var(--olive);
  }
  .reach-label {
    position: absolute; top: 346px; font-size: 24px; font-weight: 400; line-height: 1; color: var(--olive);
  }
  .map { position: absolute; background: var(--navy); }
  .map-us { left: 274px; top: 230px; width: 277px; height: 163px; border-radius: 30px 60px 40px 20px; }
  .map-world { left: 809px; top: 226px; width: 317px; height: 181px; border-radius: 40px; }
  .icon-figure { position: absolute; background: var(--navy); border-radius: 12px; }
  .icon-desk { left: 120px; top: 464px; width: 63px; height: 77px; }
  .icon-headset { left: 117px; top: 572px; width: 65px; height: 84px; }
  .learner-number {
    position: absolute; font-size: 66px; font-weight: 400; line-height: 1; color: var(--sky); white-space: nowrap;
  }
  .learner-label {
    position: absolute; font-size: 36px; font-weight: 400; line-height: 1; color: var(--navy); white-space: nowrap;
  }
  .activities-label {
    position: absolute; left: 695px; top: 535px; font-size: 25px; line-height: 32px; color: var(--navy);
  }
  .activities-number {
    position: absolute; left: 812px; top: 438px; font-size: 275px; font-weight: 400; line-height: 1;
    color: var(--sky); letter-spacing: 10px;
  }
  .views-band {
    position: absolute; left: 0; bottom: 0; width: 100%; height: 142px; background: var(--cardinal);
  }
  .views-icon { position: absolute; left: 62px; top: 18px; }
  .views-label {
    position: absolute; left: 293px; top: 13px; font-size: 29px; font-weight: 500; line-height: 37px; color: var(--white);
  }
  .views-number {
    position: absolute; left: 508px; top: 2px; font-size: 150px; font-weight: 600; line-height: 1;
    color: var(--white); letter-spacing: -4px; white-space: nowrap;
  }
</style>
</head>
<body>
<main class="infographic">
  <header class="header">
    <div class="header-virus" role="img" aria-label="Illustration of a red coronavirus particle"></div>
    <div class="brand"><span class="brand-mark"></span>Quillmere</div>
    <h1 class="title">COVID-19CME</h1>
  </header>

  <div class="reach-number" style="left:118px;">26</div>
  <div class="reach-label" style="left:132px;">STATES</div>
  <div class="map map-us" role="img" aria-label="Map of the United States"></div>

  <div class="reach-number" style="left:664px;">12</div>
  <div class="reach-label" style="left:654px;">COUNTRIES</div>
  <div class="map map-world" role="img" aria-label="World map"></div>

  <div class="icon-figure icon-desk" role="img" aria-label="Icon of a learner seated at a desk"></div>
  <div class="learner-number" style="left:232px; top:476px;">5,879</div>
  <div class="learner-label" style="left:402px; top:491px;">CME Learners</div>

  <div class="icon-figure icon-headset" role="img" aria-label="Icon of a learner with headset at a laptop"></div>
  <div class="learner-number" style="left:200px; top:599px;">23,098</div>
  <div class="learner-label" style="left:406px; top:615px;">Live Learners</div>

  <div class="activities-label"># OF<br>ACTIVITIES</div>
  <div class="activities-number">23</div>

  <section class="views-band">
    <svg class="views-icon" width="154" height="100" viewBox="0 0 154 100" aria-hidden="true">
      <path d="M36 98 C14 98 2 84 2 68 C2 52 14 40 30 40 C34 18 52 4 74 4 C96 4 112 18 116 38 C138 38 152 52 152 68 C152 86 138 98 120 98 Z" fill="#ffffff"/>
      <circle cx="78" cy="62" r="22" fill="#8c1515"/>
      <path d="M71 50 L91 62 L71 74 Z" fill="#ffffff"/>
    </svg>
    <div class="views-label"># of total<br>on-demand<br>views</div>
    <div class="views-number">1,209,987</div>
  </section>
</main>
</body>
</html>
```